Business Card Design

Im a small business that specialises in all aspects of sign installation, big and small, domestic and commercial. I have a construction and carpentry background. I'm after a professional looking business card, that has my logo as the forefront of the card incorporating the same colours as the my logo. No slogan as yet, but open to suggestions. The final design should communicate quality and class workmanship.

Target Market(s)

Managers and Owners of businesses

Industry/Entity Type

Small Business

Contact Information for Business Card

Dorian Feltwick
Mob: 0491275830
Email: dkf.fitouts@quillmail.example

Sign Installation
Property Improvement and Maintenance
Trade Services

Colors
dbdbdb
000000
ffffff

Requirements
Must have
• Logo
My name
My contact details
What I specialise in
Nice to have
• background image/images that are only just noticeable and do not take away from the logo or text.
Should not have
• No colours that contrast from my logo
No heavy machinery images to be used
Logo must stand out

```html
<!DOCTYPE html>
<html lang="en">
<head>
<meta charset="utf-8">
<title>DKF Installations — Business Card</title>
<link rel="stylesheet" href="https://fonts.googleapis.com/css2?family=Source+Sans+3:wght@400;700&display=swap">
<style>
  :root {
    --page: #e9e9e9;
    --card: #ffffff;
    --card-shade: #f2f2f2;
    --brand-blue: #1d4f9f;
    --brand-navy: #1a2f7a;
    --ink: #222222;
    --ink-soft: #6b6b6b;
    --rule: #9a9a9a;
  }
  * { box-sizing: border-box; margin: 0; padding: 0; }
  html, body { width: 1200px; height: 1012px; overflow: hidden; }
  body {
    background: var(--page);
    font-family: "Source Sans 3", "Segoe UI", sans-serif;
    color: var(--ink);
    position: relative;
  }
  .card {
    position: absolute;
    left: 220px;
    width: 760px;
    height: 430px;
    background: var(--card);
    box-shadow: 0 6px 18px rgba(0,0,0,.18);
    overflow: hidden;
  }
  .card--front { top: 60px; }
  .card--back  { top: 542px; background: linear-gradient(180deg, var(--card) 0%, var(--card-shade) 100%); }

  /* front */
  .front-texture {
    position: absolute; right: 0; top: 0; width: 62%; height: 100%;
    background: radial-gradient(ellipse at 55% 35%, #eeeeee 0%, rgba(255,255,255,0) 65%);
  }
  .front-stripe {
    position: absolute; left: 0; right: 0; bottom: 0; height: 14px;
    background: linear-gradient(90deg, rgba(29,79,159,0) 0%, var(--brand-navy) 40%, var(--brand-blue) 100%);
  }
  .front-brand {
    position: absolute; left: 56px; top: 222px;
    width: 350px;
    display: flex; align-items: center; gap: 14px;
  }
  .brand-dot {
    flex: none;
    width: 40px; height: 40px; border-radius: 50%;
    background: var(--brand-blue);
  }
  .brand-name {
    font-weight: 700; font-size: 36px; letter-spacing: 1px;
    color: var(--brand-blue); text-transform: uppercase; line-height: 1.05;
  }
  .front-brand .brand-name { max-width: 296px; }
  .contact {
    position: absolute; left: 430px; top: 112px;
    width: 320px;
    font-size: 22px; line-height: 1.3;
  }
  .contact-name { color: var(--ink); }
  .contact-role { color: var(--brand-navy); font-weight: 700; margin-bottom: 18px; }
  .contact-row { display: flex; align-items: center; gap: 12px; margin-bottom: 12px; font-size: 20px; white-space: nowrap; }
  .contact-row svg { width: 20px; height: 20px; flex: none; fill: var(--brand-navy); }

  /* back */
  .back-brand {
    position: absolute; left: 0; right: 0; top: 110px;
    display: flex; flex-direction: column; align-items: center; gap: 22px;
  }
  .back-brand .brand-dot { width: 88px; height: 88px; background: none; border: 8px solid var(--brand-blue); }
  .back-brand .brand-name { font-size: 56px; }
  .services {
    position: absolute; left: 0; right: 0; bottom: 60px;
    text-align: center; font-size: 22px; color: var(--ink-soft);
  }
  .services .sep { color: var(--rule); margin: 0 12px; }
</style>
</head>
<body>
  <section class="card card--front">
    <div class="front-texture"></div>
    <div class="front-brand">
      <span class="brand-dot"></span>
      <span class="brand-name">DKF Installations</span>
    </div>
    <div class="contact">
      <p class="contact-name">Dorian Feltwick Mob</p>
      <p class="contact-role">Managing Director</p>
      <p class="contact-row">
        <svg viewBox="0 0 24 24" aria-hidden="true"><path d="M6.6 10.8a15.2 15.2 0 0 0 6.6 6.6l2.2-2.2a1 1 0 0 1 1-.25 11.4 11.4 0 0 0 3.6.57 1 1 0 0 1 1 1V20a1 1 0 0 1-1 1A17 17 0 0 1 3 4a1 1 0 0 1 1-1h3.5a1 1 0 0 1 1 1c0 1.25.2 2.45.57 3.57a1 1 0 0 1-.25 1z"/></svg>
        <span>0491275830</span>
      </p>
      <p class="contact-row">
        <svg viewBox="0 0 24 24" aria-hidden="true"><path d="M2 5h20v14H2V5zm2 2v.4l8 5.1 8-5.1V7H4z"/></svg>
        <span>dkf.fitouts@quillmail.example</span>
      </p>
    </div>
    <div class="front-stripe"></div>
  </section>

  <section class="card card--back">
    <div class="back-brand">
      <span class="brand-dot"></span>
      <span class="brand-name">DKF Installations</span>
    </div>
    <p class="services">
      Sign Installation<span class="sep">|</span>Property improvement and maintenance<span class="sep">|</span>Trade Services
    </p>
  </section>
</body>
</html>
```